Larkspire Premium Lager beer labels

Design a beer bottle label for Larkspire Premium Lager. The beer is brewed and aged in the Williams Fork River in Colorado. The label should use the LK/antler logo and design. The label will be used on a long neck bottle so it will require a neck label (simple logo only). The beer company was established in 2020.

Target Market(s)

Consumers 21-45

Industry/Entity Type

Beverages

Requirements
Must have
• LS Logo
Should not have
• White label

```html
<!DOCTYPE html>
<html lang="en">
<head>
<meta charset="utf-8">
<title>Larkspire Premium Lager – Labels</title>
<link rel="stylesheet" href="https://fonts.googleapis.com/css2?family=Cinzel:wght@400;700&family=Noto+Serif:wght@700&family=Poppins:wght@600&display=swap">
<style>
  :root {
    --page: #efefef;
    --label-black: #141414;
    --label-edge: #1d1d1d;
    --gold: #b8955a;
    --gold-light: #d9bf8c;
    --gold-band: #c4a36b;
    --gold-dark: #7a5a2e;
    --ink-dark: #1a1206;
  }
  * { margin: 0; padding: 0; box-sizing: border-box; }
  html, body { width: 1200px; height: 960px; overflow: hidden; }
  body {
    background: var(--page);
    display: flex;
    align-items: center;
    justify-content: center;
    gap: 90px;
    font-family: "Cinzel", serif;
  }

  /* Shared band */
  .gold-band {
    height: 14px;
    background: linear-gradient(90deg, var(--gold-dark), var(--gold-band) 30%, var(--gold-light) 55%, var(--gold-band) 80%, var(--gold-dark));
  }

  /* Body label */
  .body-label {
    width: 540px;
    display: flex;
    flex-direction: column;
  }
  .body-label .panel {
    height: 684px;
    margin: 4px 0;
    background: linear-gradient(90deg, var(--label-black), var(--label-edge) 50%, var(--label-black));
    display: flex;
    flex-direction: column;
    align-items: center;
    color: var(--gold);
    text-align: center;
  }
  .established {
    margin-top: 28px;
    font-family: "Noto Serif", serif;
    font-size: 22px;
    letter-spacing: 2px;
    color: var(--gold-light);
  }
  .established-flourish {
    width: 140px;
    height: 26px;
    margin-top: 4px;
    background: linear-gradient(90deg, transparent, var(--gold-dark) 25%, var(--gold) 50%, var(--gold-dark) 75%, transparent);
    opacity: 0.55;
    border-radius: 13px;
  }

  /* Brand name set in one colour and one weight */
  .brand-mark {
    margin-top: 38px;
    display: flex;
    flex-direction: column;
    align-items: center;
    color: var(--gold);
    font-weight: 700;
  }
  .brand-mark .initials { font-size: 96px; line-height: 1; letter-spacing: 4px; }
  .brand-mark .name { margin-top: 16px; font-size: 50px; line-height: 1; letter-spacing: 2px; }
  .brand-mark .sub { margin-top: 8px; font-size: 26px; line-height: 1; letter-spacing: 2px; }

  .style-line {
    margin-top: 30px;
    font-size: 44px;
    letter-spacing: 2px;
    color: var(--gold);
  }
  .style-name {
    margin-top: 4px;
    font-size: 84px;
    font-weight: 700;
    line-height: 1.05;
    letter-spacing: 3px;
    color: var(--gold);
  }
  .tag-ribbon {
    margin-top: 18px;
    width: 380px;
    height: 36px;
    background: linear-gradient(90deg, var(--gold-dark), var(--gold-band) 40%, var(--gold-light) 60%, var(--gold-dark));
    clip-path: polygon(0 0, 100% 0, 94% 100%, 6% 100%);
    font-family: "Poppins", sans-serif;
    font-weight: 600;
    font-size: 23px;
    letter-spacing: 1px;
    color: var(--ink-dark);
    line-height: 36px;
  }
  .origin {
    margin-top: 28px;
    font-family: "Noto Serif", serif;
    font-weight: 700;
    font-size: 25px;
    line-height: 1.35;
    letter-spacing: 1px;
    color: var(--gold-light);
  }

  /* Neck label */
  .neck-label {
    width: 320px;
    display: flex;
    flex-direction: column;
  }
  .neck-label .gold-band { height: 12px; }
  .neck-label .gold-band.top { width: 234px; margin: 0 auto; }
  .neck-label .panel {
    height: 300px;
    margin: 4px 0;
    background: linear-gradient(90deg, var(--label-black), var(--label-edge) 50%, var(--label-black));
    clip-path: polygon(13% 0, 87% 0, 100% 100%, 0 100%);
    display: flex;
    flex-direction: column;
    align-items: center;
    justify-content: center;
  }
  .neck-label .brand-mark { margin-top: 10px; }
  .neck-label .brand-mark .initials { font-size: 64px; }
  .neck-label .brand-mark .name { margin-top: 14px; font-size: 32px; }
  .neck-label .brand-mark .sub { margin-top: 6px; font-size: 18px; }
</style>
</head>
<body>

  <section class="body-label" aria-label="Body label">
    <div class="gold-band"></div>
    <div class="panel">
      <p class="established">EST 2021</p>
      <div class="established-flourish" role="img" aria-label="Small hop cone with scroll flourishes"></div>
      <div class="brand-mark">
        <span class="initials">LS</span>
        <span class="name">LARKSPIRE</span>
        <span class="sub">RANCH</span>
      </div>
      <p class="style-line">PREMIUM RANCH</p>
      <h1 class="style-name">LAGER</h1>
      <p class="tag-ribbon">ORIGINAL CRAFT BEER</p>
      <p class="origin">Alder Bend River<br>High Valley</p>
    </div>
    <div class="gold-band"></div>
  </section>

  <section class="neck-label" aria-label="Neck label">
    <div class="gold-band top"></div>
    <div class="panel">
      <div class="brand-mark">
        <span class="initials">LS</span>
        <span class="name">LARKSPIRE</span>
        <span class="sub">RANCH</span>
      </div>
    </div>
    <div class="gold-band"></div>
  </section>

</body>
</html>
```